Valor Groundcrafts forestry mulching

My equipment is brand new ramtek forestry mulcher,bushhog, and dirt moving. It's a new business to me. I can much hardwoods up to 14 inch and softwood even bigger. Looking to get logo that is eye catching and something that people can remember. Love to have a picture of track skidsteer mulcher.

Target Market(s)

I'm sorry I have no idea how to do any of this guys...that's why I'm here for this to get it done. Be patient with me and I would love any feed back to help me with all this.

Contact Information for Business Card

Eye catching

Font styles to use
Sans Serif

Requirements
Must have
• Valor Groundcrafts, Greeneville Tennessee, 615 555 0193, forestry mulching, land clearing , bushhoging and dirt moving, licensed and insured, Curt Halloway ,picture of track skidsteer with mulching head.
Should not have
• Open to see anything

```html
<!DOCTYPE html>
<html lang="en">
<head>
<meta charset="utf-8">
<title>Valor Groundcrafts – Business Card Concepts</title>
<link rel="stylesheet" href="https://fonts.googleapis.com/css2?family=Anton&display=swap">
<style>
  :root {
    --paper-top: #f7f7f5;
    --paper-bottom: #e2e2da;
    --night-top: #5f6b00;
    --night-mid: #0e2300;
    --night-bottom: #031000;
    --lime: #b2d400;
    --leaf: #2f7400;
    --forest: #3d7a0a;
    --ink: #111111;
    --white: #ffffff;
    --rule-start: #3a7d0a;
    --rule-end: #e6f500;
  }
  * { box-sizing: border-box; margin: 0; padding: 0; }
  html, body { width: 1200px; height: 666px; overflow: hidden; background: var(--white); }
  body { position: relative; font-family: "Anton", "Oswald", sans-serif; }

  .card { position: absolute; overflow: hidden; }
  .card--light-front { left: 4px; top: 0; width: 588px; height: 324px;
    background: linear-gradient(to bottom, var(--paper-top), var(--paper-bottom)); }
  .card--dark-front { left: 611px; top: 0; width: 589px; height: 324px;
    background: linear-gradient(to bottom, var(--night-top), var(--night-mid) 40%, var(--night-bottom)); }
  .card--green-back { left: 0; top: 342px; width: 588px; height: 324px;
    background: linear-gradient(to bottom, var(--lime), var(--leaf) 80%); }
  .card--light-back { left: 608px; top: 342px; width: 592px; height: 324px;
    background: linear-gradient(to bottom, var(--paper-top), var(--paper-bottom)); }

  .rule { position: absolute; left: 7px; width: 575px; height: 4px; }
  .rule--gradient { background: linear-gradient(to right, var(--rule-start), var(--rule-end)); }
  .rule--white { background: var(--white); left: 11px; width: 575px; }
  .rule--green { background: var(--forest); left: 10px; width: 575px; }
  .rule--top { top: 25px; }
  .rule--bottom { top: 294px; }
  .card--green-back .rule--top, .card--light-back .rule--top { top: 24px; }
  .card--green-back .rule--bottom, .card--light-back .rule--bottom { top: 295px; }

  .brand {
    position: absolute; display: flex; flex-direction: column; align-items: center;
    text-align: center; line-height: 1; letter-spacing: 1px;
  }
  .brand__mark {
    width: 54px; height: 54px; border-radius: 50%; margin-bottom: 12px;
    border: 3px solid currentColor;
  }
  .brand__name { font-size: 40px; }
  .brand__name span { display: block; font-size: 30px; margin-top: 4px; }

  .card--light-front .brand { left: 0; right: 0; top: 78px; color: var(--forest); }
  .card--dark-front .brand { left: 0; right: 0; top: 78px; color: var(--lime); }
  .card--green-back .brand { left: 40px; width: 230px; top: 78px; color: var(--white); }
  .card--light-back .brand { left: 40px; width: 230px; top: 78px; color: var(--forest); }

  .contact {
    position: absolute; top: 78px; text-align: right; line-height: 1; letter-spacing: 0.5px;
  }
  .card--green-back .contact { right: 33px; color: var(--white); }
  .card--light-back .contact { right: 50px; color: var(--forest); }
  .contact__name { font-size: 34px; margin-bottom: 12px; }
  .contact__line { font-size: 26px; margin-bottom: 9px; }
</style>
</head>
<body>

  <section class="card card--light-front">
    <div class="rule rule--gradient rule--top"></div>
    <div class="brand">
      <div class="brand__mark"></div>
      <div class="brand__name">VALOR<span>GROUNDCRAFTS</span></div>
    </div>
    <div class="rule rule--gradient rule--bottom"></div>
  </section>

  <section class="card card--dark-front">
    <div class="rule rule--gradient rule--top"></div>
    <div class="brand">
      <div class="brand__mark"></div>
      <div class="brand__name">VALOR<span>GROUNDCRAFTS</span></div>
    </div>
    <div class="rule rule--gradient rule--bottom"></div>
  </section>

  <section class="card card--green-back">
    <div class="rule rule--white rule--top"></div>
    <div class="brand">
      <div class="brand__mark"></div>
      <div class="brand__name">VALOR<span>GROUNDCRAFTS</span></div>
    </div>
    <div class="contact">
      <p class="contact__name">NAME SURNAME</p>
      <p class="contact__line">ADDRESS</p>
      <p class="contact__line">PHONE NUMBER</p>
      <p class="contact__line">EMAIL</p>
      <p class="contact__line">WEBSITE</p>
    </div>
    <div class="rule rule--white rule--bottom"></div>
  </section>

  <section class="card card--light-back">
    <div class="rule rule--green rule--top"></div>
    <div class="brand">
      <div class="brand__mark"></div>
      <div class="brand__name">VALOR<span>GROUNDCRAFTS</span></div>
    </div>
    <div class="contact">
      <p class="contact__name">NAME SURNAME</p>
      <p class="contact__line">ADDRESS</p>
      <p class="contact__line">PHONE NUMBER</p>
      <p class="contact__line">EMAIL</p>
      <p class="contact__line">WEBSITE</p>
    </div>
    <div class="rule rule--green rule--bottom"></div>
  </section>

</body>
</html>
```